Inspiration Poster

Inspirational Poster that has a Dorin Velk like abstract look (http://www.quorvix.com/images/search?q=dorin+velk&FORM=HDRSC2) with the text:

"we walk not in order to arrive at the promise land but because walking itself is a revolution"
-Mark Fennimore

```html
<!DOCTYPE html>
<html lang="en">
<head>
<meta charset="utf-8">
<title>Walking Itself – Poster</title>
<link href="https://fonts.googleapis.com/css2?family=Jura:wght@400;500&display=swap" rel="stylesheet">
<style>
  :root {
    --tone-dark: #111010;
    --tone-storm: #3a3533;
    --tone-light: #9d9793;
    --tone-ground: #5a5450;
    --tone-deep: #2c2826;
    --caption-bg: rgba(58, 53, 50, 0.74);
    --caption-text: #f2eeea;
  }
  html, body {
    margin: 0;
    padding: 0;
    overflow: hidden;
    background: var(--tone-deep);
  }
  .poster {
    position: relative;
    width: 848px;
    height: 1200px;
    overflow: hidden;
    font-family: "Jura", sans-serif;
  }
  .poster__photo {
    position: absolute;
    inset: 0;
    background: linear-gradient(180deg,
      var(--tone-dark) 0%,
      var(--tone-storm) 28%,
      var(--tone-light) 50%,
      var(--tone-ground) 66%,
      var(--tone-deep) 100%);
  }
  .quote {
    position: absolute;
    top: 551px;
    right: 151px;
    display: flex;
    flex-direction: column;
    align-items: flex-end;
    gap: 10px;
    margin: 0;
  }
  .quote__line {
    display: block;
    background: var(--caption-bg);
    color: var(--caption-text);
    font-size: 43px;
    font-weight: 400;
    line-height: 48px;
    padding: 0 6px 0 8px;
    white-space: nowrap;
  }
  .author {
    position: absolute;
    top: 893px;
    right: 151px;
    margin: 0;
    background: var(--caption-bg);
    color: var(--caption-text);
    font-size: 30px;
    font-weight: 400;
    line-height: 41px;
    padding: 0 6px 0 14px;
    white-space: nowrap;
  }
</style>
</head>
<body>
<main class="poster">
  <div class="poster__photo" role="img" aria-label="Photograph of a dark stormy sky over the sea above a long concrete pier lined with breakwater blocks"></div>

  <blockquote class="quote">
    <span class="quote__line">“we walk</span>
    <span class="quote__line">not in order to arrive at the</span>
    <span class="quote__line">promise land</span>
    <span class="quote__line">but because walking itself</span>
    <span class="quote__line">is a revolution”</span>
  </blockquote>
  <p class="author">Mark Fennimore</p>
</main>
</body>
</html>
```